Sales Flyer Design for Cedarline Fryworks, Inc. this flyer should be bold, fun, attritive, and to the point

Our company is called Cedarline Fryworks, Inc. We collect used cooking for restaurants. We provide container for the customer to poor the frying oil into. We provide monthly rebates for cooking oil collected. We provide grease trap cleaning at charge for size of grease trap or grease interceptor. We need a flyer that is competitive and interesting to the potential customer. We would like it to be flashy and attractive. we would like a slot to leave a business card and a section to write a quote on the flyer. We want information about our company as well as the benefits of using our company. Please visit our website www.cedarlinefryworks.com to learn more about our company and what we do. We are family owned and operated. we have been in business since 1992. we service Oregon and Washington in the US. we provide the best service possible. we pick up quickly and are available for emergency calls.

Target Market(s)

Restaurants, retirement facilities, properties who manage several restaurants, sports arenas, schools, any business that has a kitchen or cooks food.

Industry/Entity Type

recycling of used cooking oils and grease trap materials

Font styles to use
Sans Serif

Colors
0054AA
0677BA
7BADD7
CADEEF
E8F1F8
0094D4
00A9DD
6FCCEA
C7EBF8
E9F6FB
59FF00
82FF00
B8FF75
E3FFCB
F4FFEA
FFF300
FFF600
FEFA6F
FFFEC7
FFFEE8
FFC000
F8CF3A
FAE287
FDF2CF
FEFAEE

Requirements
Must have
• a unique design that seperates uf from our competitors. an easy to understand and not to wordy flyer. we would like some animation such as an emoji with the money tongue hanging out when we mention rebating customers. we wants to express the hassle-free benefits of working with us. we want an emphasis on family owned since 1992
Nice to have
• cood color and balance, happy people shaking hands, images of clean oil collection containers, fancy looking vacuum trucks, overall, an engaging flyer that just doesn't get tossed in the dumpster without looking at it.
Should not have
• long paragraphs. Too much dialogue. No cliches. no boring photos.

```html
<!DOCTYPE html>
<html lang="en">
<head>
<meta charset="utf-8">
<title>Cedarline Fryworks, Inc. – Used Cooking Oil Collection Flyer</title>
<link href="https://fonts.googleapis.com/css2?family=Roboto+Condensed:wght@400;700&display=swap" rel="stylesheet">
<style>
  :root {
    --canvas-bg: #eceef0;
    --paper: #ffffff;
    --ink: #1f1f1f;
    --ink-soft: #3a3a3a;
    --black: #111111;
    --yellow-bright: #fde31b;
    --yellow-gold: #f2c230;
    --steel: #c9ccce;
    --rule: #9a9a9a;
  }
  * { box-sizing: border-box; margin: 0; padding: 0; }
  html, body { width: 1200px; height: 1200px; overflow: hidden; }
  body {
    background: var(--canvas-bg);
    font-family: "Roboto Condensed", "Arial Narrow", sans-serif;
    color: var(--ink);
    position: relative;
  }
  .flyer {
    position: absolute;
    left: 200px; top: 38px;
    width: 800px; height: 1124px;
    background: var(--paper);
    overflow: hidden;
  }
  .process-backdrop {
    position: absolute;
    left: 0; top: 683px;
    width: 800px; height: 441px;
    background: linear-gradient(100deg, #f7f4ee 0%, #fbfaf7 45%, #f2efe9 100%);
  }
  .flyer-shapes { position: absolute; inset: 0; }
  .brand-name {
    position: absolute;
    right: 70px; top: 100px;
    color: #ffffff;
    font-weight: 700;
    font-size: 30px;
    letter-spacing: 1px;
    text-align: right;
    line-height: 1.05;
  }
  .brand-tagline {
    position: absolute;
    right: 70px; top: 140px;
    color: var(--yellow-bright);
    font-size: 15px;
    letter-spacing: 3px;
    text-transform: uppercase;
  }
  .headline {
    position: absolute;
    right: 60px; top: 406px;
    width: 340px;
    text-align: right;
    font-weight: 700;
    font-size: 27px;
    line-height: 32px;
    color: var(--ink);
  }
  .intro {
    position: absolute;
    left: 223px; top: 561px;
    width: 544px;
    font-size: 10.5px;
    line-height: 15px;
    color: var(--ink-soft);
  }
  .intro strong { color: var(--ink); }
  .section-band {
    position: absolute;
    left: 0; top: 683px;
    width: 437px; height: 52px;
    background: var(--yellow-gold);
    padding-left: 48px;
    font-weight: 700;
    font-size: 35px;
    line-height: 52px;
    color: var(--ink);
  }
  .process-copy {
    position: absolute;
    left: 48px; top: 762px;
    width: 704px;
    font-size: 10.5px;
    line-height: 15px;
    color: var(--ink-soft);
  }
  .process-copy ul { list-style: none; }
  .process-copy li::before { content: "\2022  "; }
  .process-copy strong { color: var(--ink); }
  .quote-box {
    position: absolute;
    left: 48px; top: 880px;
    width: 380px;
  }
  .quote-box h3, .card-slot span {
    font-size: 13px;
    font-weight: 700;
    color: var(--ink);
    text-transform: uppercase;
    letter-spacing: 1px;
  }
  .quote-line {
    display: flex;
    align-items: flex-end;
    gap: 8px;
    height: 24px;
    font-size: 10.5px;
    color: var(--ink-soft);
  }
  .quote-line i { flex: 1; border-bottom: 1px solid var(--rule); height: 1px; }
  .card-slot {
    position: absolute;
    right: 48px; top: 876px;
    width: 200px; height: 114px;
    border: 1.5px dashed var(--rule);
    display: flex;
    align-items: center;
    justify-content: center;
  }
  .card-slot span { font-size: 11px; color: var(--rule); }
  .footer-company {
    position: absolute;
    left: 48px; top: 1030px;
    font-style: normal;
  }
  .footer-company h2 {
    font-size: 19px;
    font-weight: 700;
    margin-bottom: 8px;
  }
  .address {
    font-size: 12px;
    line-height: 19px;
    color: var(--ink-soft);
    padding-left: 18px;
    position: relative;
  }
  .address svg { position: absolute; left: 0; top: 4px; }
  .contact-list {
    position: absolute;
    right: 48px; top: 1040px;
    list-style: none;
    text-align: right;
    font-size: 12px;
    line-height: 20px;
    color: var(--ink-soft);
  }
  .contact-list li { display: flex; justify-content: flex-end; align-items: center; gap: 8px; }
  .contact-list svg { flex: none; }
</style>
</head>
<body>
  <main class="flyer">
    <div class="process-backdrop" role="img" aria-label="Faint background photo of a commercial kitchen"></div>

    <svg class="flyer-shapes" width="800" height="1124" viewBox="0 0 800 1124">
      <defs>
        <linearGradient id="fryer-tones" x1="0" y1="0" x2="1" y2="1">
          <stop offset="0" stop-color="#d8dadb"/>
          <stop offset="0.35" stop-color="#c9ccce"/>
          <stop offset="0.55" stop-color="#e9c25a"/>
          <stop offset="0.8" stop-color="#f3d98a"/>
          <stop offset="1" stop-color="#a7a39a"/>
        </linearGradient>
      </defs>
      <polygon class="top-wedge" points="67,0 333,0 200,73" fill="var(--yellow-bright)"/>
      <polygon class="hero-photo" role="img" aria-label="Photo of a stainless steel deep fryer with bubbling golden oil and a wire basket"
        points="0,0 40,0 150,59 564,324 0,652" fill="url(#fryer-tones)"/>
      <polygon class="brand-panel" points="353,0 800,0 800,420 233,100" fill="var(--black)"/>
      <polygon class="footer-black" points="453,1017 667,1124 400,1124" fill="var(--black)"/>
      <polygon class="footer-yellow" points="347,1017 560,1124 120,1124" fill="var(--yellow-gold)"/>
    </svg>

    <div class="brand-name">CEDARLINE FRYWORKS, INC.</div>
    <div class="brand-tagline">Family owned since 1992</div>

    <h1 class="headline">Used Cooking Oil<br>Collection in the Portland,<br>OR Metro Area and<br>Southern Washington</h1>

    <p class="intro">Your fryer oil pays you back. <strong>Cedarline Fryworks is family owned and operated since 1992</strong>, serving kitchens across Oregon and Washington. We drop off clean containers, pick up fast and send you a <strong>rebate every month</strong> for the oil we collect. No mess, no hassle – just pour, close the lid and we handle the rest.</p>

    <h2 class="section-band">Our Maintenance Process</h2>

    <div class="process-copy">
      <ul>
        <li><strong>Free containers</strong> – clean, sealed and sized for your kitchen.</li>
        <li><strong>Monthly rebates</strong> – cash back for every gallon of used oil we collect.</li>
        <li><strong>Grease trap cleaning</strong> – priced by the size of your trap or interceptor; FOG levels reported to the city.</li>
        <li><strong>Quick pickups &amp; emergency calls</strong> – a technician on the way when you need one.</li>
      </ul>
    </div>

    <section class="quote-box" aria-label="Quote">
      <h3>Your Quote</h3>
      <div class="quote-line">Oil pickup:<i></i></div>
      <div class="quote-line">Grease trap:<i></i></div>
      <div class="quote-line">Monthly rebate:<i></i></div>
    </section>

    <div class="card-slot"><span>Business card here</span></div>

    <address class="footer-company">
      <h2>Cedarline Fryworks, Inc.</h2>
      <p class="address">
        <svg width="9" height="11" viewBox="0 0 9 11"><path d="M4.5 0A4 4 0 0 0 .5 4c0 3 4 7 4 7s4-4 4-7a4 4 0 0 0-4-4zm0 5.5A1.5 1.5 0 1 1 4.5 2.5a1.5 1.5 0 0 1 0 3z" fill="var(--ink)"/></svg>
        1480 NW Alder Ave.<br>Portland, OR 97209
      </p>
    </address>

    <ul class="contact-list">
      <li>503.555.0142
        <svg width="11" height="11" viewBox="0 0 11 11"><path d="M2.3 0.6l1.6 2.1-.9 1.2c.6 1.3 1.6 2.3 2.9 2.9l1.2-.9 2.1 1.6-.8 1.8C5 9.2 1.6 5.8 0.5 1.4z" fill="var(--ink)"/></svg>
      </li>
      <li>sales@cedarlinefryworks.com
        <svg width="11" height="11" viewBox="0 0 11 11"><rect x="0.5" y="2" width="10" height="7" fill="var(--ink)"/><path d="M0.5 2l5 3.8 5-3.8" stroke="#fff" stroke-width="0.9" fill="none"/></svg>
      </li>
      <li>www.cedarlinefryworks.com
        <svg width="11" height="11" viewBox="0 0 11 11"><circle cx="5.5" cy="5.5" r="4.8" fill="none" stroke="var(--ink)" stroke-width="1.2"/><path d="M0.7 5.5h9.6M5.5 0.7c-2.4 2.6-2.4 7 0 9.6M5.5 0.7c2.4 2.6 2.4 7 0 9.6" stroke="var(--ink)" stroke-width="0.9" fill="none"/></svg>
      </li>
    </ul>
  </main>
</body>
</html>
```